New Business Card Design Project

We need to enhance the look and feel of our brand. We are starting with the business card and will hopefully expand to letter head, website, etc. The firm is based in Kolding Denmark and invests with global pension funds and for mutual fund investors alike. We would like to see an innovative use of the companies logo (star on the website - www.tidemarkharbor.com) and a broader use of a color palette. Presently it is dominantly shades of blue. The firm wants to convey a sense they are a creative investment team that understands all the risks in the emerging markets and have the skills to perform in an environment of uncertainty.

Presently, we have three locations: Kolding Denmark, Glendale CA USA, Zurich Switzerland. We also have a prominently displayed bar code square on a solid dark blue back that will take smart phone users to the firm's website. I am indifferent to its inclusion., Details for my new Business Card Design Project will be added soon.
Updates

Reason: Designers, I am working with on getting feedback from both US and Danish partners on preferences. That is taking slightly more time than expected. Thanks for you patience. Nice work. PLM

Target Market(s)

The target market is a combination of institutional and retail investors. The european arm uses a card similar to a couple of those submitted.

Industry/Entity Type

Environment

Requirements
Must have
• The company's Star Logo. See www.tidemarkharbor.com. It may be used in its current form or some new clever way. The founders are Danish and have a strong affinity for it.
Nice to have
• The new materials may be solely used in the north America and distributed in Australia as well. Therefore, we may try something new in these markets. I'd prefer to see a broader use of the color spectrum, not simply blue.
Should not have
• The card should not look and feel like a bank, insurance company, or a traditional money manager.

```html
<!DOCTYPE html>
<html lang="en">
<head>
<meta charset="utf-8">
<title>Tidemark Harbor – Business Card</title>
<link rel="stylesheet" href="https://fonts.googleapis.com/css2?family=Archivo:wght@300;400;700&display=swap">
<style>
  :root {
    --band-cyan: #5ff3ff;
    --paper: #ffffff;
    --ink-dark: #231f20;
    --ink-light: #ffffff;
    --mark-navy: #0c3a85;
    --wordmark: #5ff3ff;
  }
  html, body {
    margin: 0;
    padding: 0;
    width: 1200px;
    height: 721px;
    overflow: hidden;
    background: var(--paper);
  }
  .card {
    position: relative;
    width: 1200px;
    height: 721px;
    background: var(--paper);
    font-family: "Archivo", Helvetica, Arial, sans-serif;
    overflow: hidden;
  }
  .contact-band {
    position: absolute;
    left: 0;
    top: 0;
    width: 1200px;
    height: 491px;
    background: var(--band-cyan);
  }
  .person-name {
    position: absolute;
    left: 86px;
    top: 74px;
    margin: 0;
    font-size: 46px;
    font-weight: 700;
    color: var(--ink-light);
    line-height: 1;
  }
  .person-role {
    position: absolute;
    left: 86px;
    top: 134px;
    margin: 0;
    font-size: 34px;
    font-weight: 400;
    color: var(--ink-dark);
    line-height: 1;
  }
  .contact-lines {
    position: absolute;
    left: 86px;
    top: 226px;
    margin: 0;
    font-size: 36px;
    font-weight: 300;
    color: var(--ink-light);
    line-height: 48px;
    font-style: normal;
  }
  .contact-lines span { display: block; }
  .brand-lockup {
    position: absolute;
    left: 306px;
    top: 532px;
    height: 114px;
    display: flex;
    align-items: center;
    gap: 30px;
  }
  .brand-dot { width: 114px; height: 114px; display: block; }
  .brand-name {
    font-size: 88px;
    font-weight: 400;
    color: var(--wordmark);
    line-height: 1;
    letter-spacing: 1px;
  }
</style>
</head>
<body>
  <main class="card">
    <section class="contact-band">
      <h1 class="person-name">Erik N. Halvorsen</h1>
      <p class="person-role">Founder</p>
      <address class="contact-lines">
        <span class="contact-email">erikhalvorsen@mailbox.com</span>
        <span class="contact-phone">(+01)5550148273</span>
      </address>
    </section>
    <div class="brand-lockup">
      <svg class="brand-dot" viewBox="0 0 114 114" aria-hidden="true">
        <circle cx="57" cy="57" r="57" fill="var(--mark-navy)"/>
      </svg>
      <span class="brand-name">TidemarkHarbor</span>
    </div>
  </main>
</body>
</html>
```